Business cards and stationary for IT Service Provider
Orlen Datacraft
Business cards and stationary for IT Service Provider - Information Technology
Creative Brief
Use specific fonts
No preference, we have used is called ETHNOCENTRIC for the tagline
Bright & Fun-filled
Peter Hollins
Director
Meadowbank Upper Fenwick Lane Brindlow, Preston PR5 7QT
pete@orlendatacraft-mail.com
www.orlendatacraft-mail.com
VAT Number and company registration number to be included somewhere on business card. VAT Number: 846 227 51 Company Registration Number: 4918264 In addition to letterhead we would also like a continuation sheet.
All the information we require is listed above, everything else is entirely up to you!
orlendatacraft orlendatacraft
Please note that this project is for Business Cards AND Stationary. Could we see some Letterheads too?

```html
<!DOCTYPE html>
<html lang="en">
<head>
<meta charset="utf-8">
<title>Kestrano Datacraft — Stationery Set</title>
<link href="https://fonts.googleapis.com/css2?family=Michroma&family=Open+Sans:wght@400;600;700&display=swap" rel="stylesheet">
<style>
  :root {
    --brand-red: #e5141f;
    --ink: #222222;
    --muted: #6b6b6b;
    --paper: #ffffff;
    --backdrop: #eeeeee;
    --edge: #dedede;
  }
  * { box-sizing: border-box; margin: 0; padding: 0; }
  html, body { width: 1200px; height: 936px; overflow: hidden; }
  body {
    position: relative;
    background: var(--backdrop);
    font-family: "Open Sans", Arial, sans-serif;
    color: var(--ink);
  }
  .sheet { position: absolute; background: var(--paper); border: 1px solid var(--edge); overflow: hidden; }

  .wordmark {
    font-family: "Michroma", "Arial Black", sans-serif;
    color: var(--brand-red);
    text-transform: uppercase;
    font-weight: 400;
    line-height: 1.15;
    letter-spacing: 0.04em;
    display: inline-block;
    white-space: nowrap;
  }

  /* Letterhead */
  .letterhead { left: 183px; top: 63px; width: 394px; height: 550px; }
  .letterhead .edge-band { position: absolute; left: 0; top: 0; width: 14px; height: 100%; background: var(--brand-red); }
  .letterhead .wordmark { position: absolute; left: 42px; top: 42px; font-size: 12px; }
  .letterhead .contact-block { position: absolute; left: 262px; top: 34px; font-size: 5px; line-height: 2; color: var(--muted); }
  .contact-block .dot { display: inline-block; width: 4px; height: 4px; background: var(--brand-red); margin-right: 4px; vertical-align: middle; }
  .letter-body { position: absolute; left: 42px; top: 130px; width: 320px; font-size: 5.4px; line-height: 2.1; color: var(--muted); }
  .letter-body p { margin-bottom: 12px; }
  .letter-body .signature { width: 40px; height: 14px; background: linear-gradient(90deg, #cfcfcf, #9a9a9a); border-radius: 7px; margin: 6px 0 10px; }
  .letter-body .sender { color: var(--ink); font-weight: 600; }

  /* Folder */
  .folder { left: 634px; top: 38px; width: 468px; height: 580px; }
  .folder .spine { position: absolute; left: 0; top: 0; width: 38px; height: 100%; background: var(--brand-red); }
  .folder .spine-url {
    position: absolute; left: 19px; top: 50%;
    transform: translate(-50%, -50%) rotate(-90deg);
    white-space: nowrap; color: #fff; font-size: 9px; letter-spacing: 0.2em;
  }
  .folder .wordmark { position: absolute; left: 253px; top: 290px; transform: translate(-50%, -50%); font-size: 22px; text-align: center; }

  /* Business cards */
  .card-front { left: 46px; top: 654px; width: 178px; height: 116px; }
  .card-front .wordmark { position: absolute; left: 10px; top: 46px; font-size: 6px; }
  .card-front .info-panel { position: absolute; right: 0; top: 0; width: 80px; height: 100%; background: var(--brand-red); color: #fff; padding: 10px 6px; }
  .info-panel .lines { font-size: 3.4px; line-height: 2; }
  .info-panel .holder { position: absolute; left: 6px; bottom: 12px; }
  .info-panel .holder-name { font-size: 5.5px; font-weight: 700; text-transform: uppercase; }
  .info-panel .holder-role { font-size: 4.5px; text-transform: uppercase; letter-spacing: 0.08em; }

  .card-back { left: 46px; top: 781px; width: 178px; height: 102px; display: flex; align-items: center; justify-content: center; }
  .card-back .wordmark { font-size: 7px; text-align: center; }

  /* Envelopes */
  .envelope-front { left: 266px; top: 672px; width: 432px; height: 208px; }
  .envelope-front .edge-band { position: absolute; left: 0; top: 0; width: 12px; height: 100%; background: var(--brand-red); }
  .envelope-front .wordmark { position: absolute; left: 38px; top: 38px; font-size: 14px; }

  .envelope-back { left: 738px; top: 672px; width: 424px; height: 208px; }
  .envelope-back .flap { position: absolute; left: 0; top: 0; }
  .envelope-back .flap-url { position: absolute; left: 0; top: 26px; width: 100%; text-align: center; color: #fff; font-size: 11px; letter-spacing: 0.22em; }
</style>
</head>
<body>

  <section class="sheet letterhead" aria-label="Letterhead">
    <div class="edge-band"></div>
    <div class="wordmark">Kestrano<br>Datacraft</div>
    <div class="contact-block">
      <div><span class="dot"></span>Meadowbank Upper Fenwick Lane</div>
      <div><span class="dot"></span>Brindlow, Preston PR5 7QT</div>
      <div><span class="dot"></span>pete@kestranodatacraft-mail.com</div>
      <div><span class="dot"></span>www.kestranodatacraft-mail.com</div>
    </div>
    <div class="letter-body">
      <p>12 June 2024</p>
      <p>Dear Client,<br>Client Name<br>14 High Street, Preston</p>
      <p>Thank you for choosing our team for your network upgrade. We have reviewed the current setup at your offices and prepared a clear plan covering servers, backups, remote access and staff support, with each stage priced and scheduled below for your review.</p>
      <p>Our engineers will begin with a full audit in the first week, followed by installation and testing. Work can be carried out after hours to avoid disruption.</p>
      <p>Once the new systems are live, we will provide ongoing monitoring, monthly reports and a dedicated help line for your staff. Please contact us with any questions about the proposal or the timeline, and we will be glad to arrange a meeting at a time that suits you.</p>
      <p>Yours sincerely,</p>
      <div class="signature" role="img" aria-label="Handwritten signature"></div>
      <p><span class="sender">Peter Hollins</span><br>Director<br>Meadowbank Upper Fenwick Lane Brindlow, Preston PR5 7QT</p>
    </div>
  </section>

  <section class="sheet folder" aria-label="Presentation folder">
    <div class="spine"><span class="spine-url">www.kestranodatacraft-mail.com</span></div>
    <div class="wordmark">Kestrano<br>Datacraft</div>
  </section>

  <section class="sheet card-front" aria-label="Business card front">
    <div class="wordmark">Kestrano<br>Datacraft</div>
    <div class="info-panel">
      <div class="lines">
        pete@kestranodatacraft-mail.com<br>
        www.kestranodatacraft-mail.com<br>
        VAT No: 846 227 51<br>
        Reg No: 4918264
      </div>
      <div class="holder">
        <div class="holder-name">Peter Hollins</div>
        <div class="holder-role">Director</div>
      </div>
    </div>
  </section>

  <section class="sheet card-back" aria-label="Business card back">
    <div class="wordmark">Kestrano<br>Datacraft</div>
  </section>

  <section class="sheet envelope-front" aria-label="Envelope front">
    <div class="edge-band"></div>
    <div class="wordmark">Kestrano<br>Datacraft</div>
  </section>

  <section class="sheet envelope-back" aria-label="Envelope back">
    <svg class="flap" width="424" height="120" viewBox="0 0 424 120">
      <path d="M0 0 H424 V60 Q212 128 0 60 Z" fill="var(--brand-red)"/>
    </svg>
    <div class="flap-url">www.kestranodatacraft-mail.com</div>
  </section>

</body>
</html>
```